Business Card Design for BrightlaneReach.com

--I need a business card design for my company BrightlaneReach.com

I have attached my logo...I want the brightlane reach logo on the front of the business card, and then I want The Brightlane Chief on the back of it with my information.

I would like to see a light colored background as well as a dark colored background

FRONT:
BRIGHTLANE REACH LOGO
247 E. Pelham Row
5th Floor
San Diego CA 92384
www.BrightlaneReach.com

Advanced Website & App Development
Websites, Apps, Online Voucher Systems

Leading Edge Marketing Services
SMS, VB, SMM, SEM,

BACK:
BRIGHTLANE CHIEF LOGO
Dorian Welker
The Brightlane Chief
Call Or Text: 555-204-3378
Dorian@BrightlaneChief.com
www.BrightlaneChief.com

Target Market(s)

small business owners

Industry/Entity Type

Business Consultant

Contact Information for Business Card

FRONT:
BRIGHTLANE REACH LOGO
247 E. Pelham Row
5th Floor
San Diego CA 92384
www.BrightlaneReach.com

SMS, VB, SMM, SEM,

BACK:
BRIGHTLANE CHIEF LOGO
Dorian Welker
The Brightlane Chief
Dorian@BrightlaneChief.com
www.BrightlaneChief.com

Requirements
Must have
• add this quote on it somewhere, anywhere,preferrably on back
• "The Fastest Way To Success Is To Take Action”
• — Dorian Welker, Brightlane Chief
Nice to have
• open
Should not have
• red

```html
<!DOCTYPE html>
<html lang="en">
<head>
<meta charset="utf-8">
<title>Brightlane Reach Business Cards</title>
<link href="https://fonts.googleapis.com/css2?family=Arimo:ital,wght@0,400;0,700;1,400&display=swap" rel="stylesheet">
<style>
  :root {
    --backdrop: #3a3431;
    --card: #141414;
    --accent: #1b86c9;
    --ink-light: #f2f2f2;
    --ink-muted: #a8a8a8;
  }
  html, body {
    margin: 0;
    padding: 0;
    width: 1200px;
    height: 780px;
    overflow: hidden;
    background: var(--backdrop);
    font-family: "Arimo", Arial, sans-serif;
  }
  .canvas {
    position: relative;
    width: 1200px;
    height: 780px;
  }
  .card {
    position: absolute;
    width: 540px;
    height: 308px;
    background: var(--card);
    border-radius: 4px;
    box-shadow: 0 14px 30px rgba(0,0,0,0.55);
    overflow: hidden;
  }
  .card--chief { left: 50px; top: 110px; }
  .card--reach { left: 610px; top: 362px; }

  .card__divider {
    position: absolute;
    top: 50px;
    bottom: 50px;
    width: 2px;
    background: var(--accent);
  }
  .card--chief .card__divider { left: 268px; }
  .card--reach .card__divider { left: 258px; }

  .brand-name {
    position: absolute;
    top: 50%;
    transform: translateY(-50%);
    color: var(--accent);
    font-weight: 400;
    font-size: 19px;
    letter-spacing: 1.5px;
    text-align: center;
    white-space: nowrap;
  }
  .card--chief .brand-name { left: 14px; width: 240px; }
  .card--reach .brand-name { left: 10px; width: 234px; }

  .details {
    position: absolute;
    top: 0;
    bottom: 0;
    display: flex;
    flex-direction: column;
    justify-content: center;
  }
  .card--chief .details { left: 294px; right: 18px; }
  .card--reach .details { left: 268px; right: 8px; align-items: center; text-align: center; }

  .person-name {
    color: var(--ink-light);
    font-weight: 700;
    font-size: 20px;
    letter-spacing: 0.5px;
    margin: 0;
    white-space: nowrap;
  }
  .person-title {
    color: var(--ink-light);
    font-size: 12px;
    letter-spacing: 0.8px;
    margin: 2px 0 26px;
    white-space: nowrap;
  }
  .contact-line {
    color: var(--accent);
    font-size: 15px;
    line-height: 1.3;
    margin: 0;
    white-space: nowrap;
  }
  .quote {
    color: var(--ink-muted);
    font-size: 10.5px;
    font-style: italic;
    line-height: 1.4;
    margin: 18px 0 0;
  }
  .address-line {
    color: var(--accent);
    font-size: 12.5px;
    line-height: 1.35;
    margin: 0;
    white-space: nowrap;
  }
  .services {
    margin-top: 18px;
  }
  .service-line {
    color: var(--ink-light);
    font-size: 13px;
    line-height: 1.35;
    margin: 0;
    white-space: nowrap;
  }
</style>
</head>
<body>
<main class="canvas">

  <section class="card card--chief" aria-label="Back of card">
    <div class="brand-name">BRIGHTLANE CHIEF</div>
    <div class="card__divider"></div>
    <div class="details">
      <p class="person-name">DORIAN WELKER</p>
      <p class="person-title">THE BRIGHTLANE CHIEF</p>
      <p class="contact-line">555-204-3378</p>
      <p class="contact-line">Dorian@BrightlaneChief.com</p>
      <p class="contact-line">www.BrightlaneChief.com</p>
      <p class="quote">“The Fastest Way To Success Is To Take Action”<br>— Dorian Welker, Brightlane Chief</p>
    </div>
  </section>

  <section class="card card--reach" aria-label="Front of card">
    <div class="brand-name">BRIGHTLANE REACH</div>
    <div class="card__divider"></div>
    <div class="details">
      <p class="address-line">www.BrightlaneReach.com</p>
      <p class="address-line">247 E. Pelham Row 5th Floor San Diego</p>
      <p class="address-line">CA 92384</p>
      <div class="services">
        <p class="service-line">Advanced Website &amp; App Development</p>
        <p class="service-line">Websites,Apps, Online Voucher Systems</p>
        <p class="service-line">Leading Edge Marketing ServicesSMS,</p>
        <p class="service-line">VB, SMM, SEM,</p>
      </div>
    </div>
  </section>

</main>
</body>
</html>
```